Neudesign von Visitenkarten und Briefpapier für Eventmanager
Zielgruppe
Als Eventmanager bin ich seit mehr als 15 Jahren in verschiedenen Tätigkeitsfeldern und Veranstaltungsbereichen tätig.
Wechselnde Auftraggeber, Arbeitsfelder und Themen prägen meinen beruflichen Alltag.
Die Bandbreite der Tätigkeiten reicht von Organisation und Durchführung über Konzeption und Planung bis zu Management und Beratung.
Schwerpunkt und Gemeinsamkeit ist eine planerische Tätigkeit mit Umsetzung vor Ort.
Das Wort Produktionsbüro spielt in meinen Tätigkeiten immer eine große Rolle. Produktionsbüros sind die zentrale Schaltstelle bei Veranstaltungen.
Die Domain www.stagewerkraum.de ist meine. (es gibt keinen Internetauftritt)
Bereiche: Corporate Events, Entertainment und Musik-Tourneen, Ausstellungen
international tätig
Auftraggeber sind sowohl Endkunden als auch Agenturen aus den verschiedenen Bereichen. (Eventagenturen, Tournee- und Konzertveranstalter, internationale Ausstellungsgesellschaften)
Aufgabenstellung
Entwicklung einer Wort-/Bildmarke
Stichworte: sachlich, schnörkellos, klar, nicht verspielt, zeitlos
Gestaltung von Visitenkarten und Briefpapier
Das Design muß sich ändern lassen (z.B. Umzug) und rein digital verwendbar sein – kein Druck von Briefpapier, sondern Korrespondenz lediglich digital aus MS Word/Word für MAC.
Mögliche Ansätze:
„Dorbusch“ als Personen- und Markennamen hervorheben
„venue desk“ als überspannenden Tätigkeitsbegriff und -namen hervorheben
Das Design sollte s/w (Grautöne) oder farblich dezent sein (1 Farbe + Grau).
Im Anhang mein derzeitiges Briefpapier und die Visitenkarte. Alle diese Information sollen auch zukünftig Platz finden.

```html
<!DOCTYPE html>
<html lang="de">
<head>
<meta charset="utf-8">
<title>venue desk – Visitenkarten</title>
<link rel="stylesheet" href="https://fonts.googleapis.com/css2?family=Didact+Gothic&family=Open+Sans:wght@400&family=Archivo:ital,wght@1,800&display=swap">
<style>
  :root {
    --bg: #ececec;
    --card: #3c3c3e;
    --text: #e6e6e6;
    --muted: #cfcfcf;
    --accent: #d0571f;
    --silver: #d9d9db;
    --gold: #d8b23a;
    --shadow: rgba(0, 0, 0, 0.28);
  }
  * { margin: 0; padding: 0; box-sizing: border-box; }
  html, body {
    width: 1200px;
    height: 900px;
    overflow: hidden;
    background: var(--bg);
  }
  .sheet {
    position: relative;
    width: 1200px;
    height: 900px;
    display: grid;
    grid-template-columns: 500px 500px;
    grid-template-rows: 310px 310px;
    column-gap: 60px;
    row-gap: 90px;
    justify-content: center;
    align-content: center;
  }
  .card {
    position: relative;
    background: var(--card);
    box-shadow: 0 4px 10px var(--shadow);
    color: var(--text);
    overflow: hidden;
  }
  .card--silver { --metal: var(--silver); }
  .card--gold { --metal: var(--gold); }

  /* front */
  .wordmark {
    position: absolute;
    left: 70px;
    top: 30px;
    font-family: "Didact Gothic", sans-serif;
    font-size: 64px;
    line-height: 1;
    letter-spacing: -1px;
    color: var(--metal);
  }
  .wordmark-rule {
    position: absolute;
    left: 70px;
    right: 36px;
    top: 103px;
    height: 3px;
    background: var(--metal);
  }
  .tagline {
    position: absolute;
    right: 36px;
    top: 112px;
    font-family: "Didact Gothic", sans-serif;
    font-size: 20px;
    letter-spacing: 3px;
    color: var(--muted);
  }
  .services {
    position: absolute;
    right: 40px;
    top: 165px;
    list-style: none;
    text-align: right;
    font-family: "Didact Gothic", sans-serif;
    font-size: 12px;
    line-height: 20px;
    letter-spacing: 3.5px;
    color: var(--muted);
  }
  .services .highlight { color: var(--accent); }

  /* back */
  .holder {
    position: absolute;
    left: 0;
    right: 0;
    top: 110px;
    text-align: center;
    font-family: "Archivo", sans-serif;
    font-style: italic;
    font-weight: 800;
    font-size: 20px;
    color: var(--metal);
  }
  .contact {
    position: absolute;
    left: 0;
    right: 0;
    bottom: 30px;
    text-align: center;
    font-family: "Open Sans", sans-serif;
    font-size: 14px;
    line-height: 20px;
    color: var(--text);
  }
  .contact .dot {
    display: inline-block;
    width: 5px;
    height: 5px;
    border-radius: 50%;
    background: var(--metal);
    vertical-align: middle;
    margin: 0 5px 2px;
  }
</style>
</head>
<body>
<main class="sheet">
  <section class="card card--silver card-front">
    <div class="wordmark">dorbusch</div>
    <div class="wordmark-rule"></div>
    <div class="tagline">venue desk</div>
    <ul class="services">
      <li>konzeption</li>
      <li>organisation</li>
      <li>corporate <span class="highlight">event</span></li>
      <li class="highlight">management</li>
      <li>entertainment</li>
      <li>ausstellung</li>
    </ul>
  </section>

  <section class="card card--gold card-front">
    <div class="wordmark">dorbusch</div>
    <div class="wordmark-rule"></div>
    <div class="tagline">venue desk</div>
    <ul class="services">
      <li>konzeption</li>
      <li>organisation</li>
      <li>corporate <span class="highlight">event</span></li>
      <li class="highlight">management</li>
      <li>entertainment</li>
      <li>ausstellung</li>
    </ul>
  </section>

  <section class="card card--silver card-back">
    <p class="holder">martin dorbusch</p>
    <address class="contact">
      venue desk<span class="dot"></span>lindenweg 7<span class="dot"></span>42853 remscheid<br>
      T: +49 (0) 170 318 522<span class="dot"></span>F: +49 (0) 212 480 167 39<br>
      dorbusch@stagewerkraum.de
    </address>
  </section>

  <section class="card card--gold card-back">
    <p class="holder">martin dorbusch</p>
    <address class="contact">
      venue desk<span class="dot"></span>lindenweg 7<span class="dot"></span>42853 remscheid<br>
      T: +49 (0) 170 318 522<span class="dot"></span>F: +49 (0) 212 480 167 39<br>
      dorbusch@stagewerkraum.de
    </address>
  </section>
</main>
</body>
</html>
```